BOLD & MINIMALIST DESIGN NEEDED

We want a very bold but minimalistic business card design that is impactful and utilizes both sides of the business card. Our current logo is included for your use.

We want bold fonts and good use of negative space. We don't want the logo to overpower the design.

Target Market(s)

Professionals who are building new commercial buildings.

Industry/Entity Type

Construction

Contact Information for Business Card

Name, Title, email, office phone, cell phone, website

Font styles to use
Serif
Sans Serif

Requirements
Must have
• Bold design!

```html
<!DOCTYPE html>
<html lang="en">
<head>
<meta charset="utf-8">
<title>Ridgeway Design + Build – Business Card</title>
<link rel="stylesheet" href="https://fonts.googleapis.com/css2?family=Open+Sans:wght@400;600;800&display=swap">
<style>
  :root {
    --ink: #0b0c0c;
    --paper: #ffffff;
    --paper-shade: #ececec;
    --green: #76bd3a;
    --green-light: #a8d97c;
    --text-grey: #3d3d3d;
    --stage: #e4e2df;
  }
  * { box-sizing: border-box; margin: 0; padding: 0; }
  html, body {
    width: 1200px; height: 900px; overflow: hidden;
    background: var(--stage);
    font-family: "Open Sans", Arial, sans-serif;
  }
  .canvas { position: relative; width: 1200px; height: 900px; }

  .card {
    position: absolute; width: 700px; height: 400px; overflow: hidden;
    background: linear-gradient(120deg, var(--paper-shade), var(--paper) 60%);
    box-shadow: 0 10px 28px rgba(0,0,0,.22);
  }
  .card--front { left: 60px; top: 50px; }
  .card--back  { left: 440px; top: 460px; }
  .card__art { position: absolute; inset: 0; width: 100%; height: 100%; }

  .wordmark {
    position: absolute; display: flex; align-items: center; gap: 10px;
    color: var(--ink); font-weight: 800; text-transform: uppercase;
    line-height: 1;
  }
  .wordmark__square { width: 22px; height: 22px; background: var(--green); flex: none; }
  .wordmark__name { font-size: 30px; letter-spacing: .5px; }
  .wordmark__name small { display: block; font-size: 13px; letter-spacing: 5px; margin-top: 6px; }

  .card--front .wordmark { left: 70px; top: 160px; }
  .front__web {
    position: absolute; left: 72px; top: 250px;
    color: var(--green); font-weight: 600; font-size: 17px; letter-spacing: 9px;
  }

  .card--back .wordmark { left: 400px; top: 34px; }

  .contact { position: absolute; left: 292px; top: 108px; color: var(--text-grey); font-size: 16px; }
  .contact__name { color: var(--ink); font-weight: 800; font-size: 21px; line-height: 1.35; }
  .contact__title { font-size: 17px; margin-bottom: 4px; line-height: 1.35; }
  .contact__line { display: flex; align-items: center; gap: 9px; height: 25px; }
  .contact__line svg { width: 16px; height: 16px; flex: none; }
  .contact__list { margin-top: 2px; }
  .contact__list .contact__line:first-child { margin-bottom: 8px; }
  .accent { color: var(--green); }
  .contact__address { margin-top: 14px; line-height: 1.4; }
</style>
</head>
<body>
<main class="canvas">

  <section class="card card--front">
    <svg class="card__art" viewBox="0 0 700 400">
      <g role="img" aria-label="Large brand mark decoration area">
        <rect x="440" y="0" width="260" height="330" fill="var(--ink)"/>
        <rect x="470" y="120" width="90" height="60" fill="var(--green)"/>
      </g>
      <path d="M300,400 C430,385 560,330 700,245 L700,400 Z" fill="var(--paper)"/>
      <path d="M330,400 C450,380 570,325 700,262 L700,400 Z" fill="var(--ink)"/>
    </svg>
    <div class="wordmark">
      <span class="wordmark__square"></span>
      <span class="wordmark__name">Ridgeway<small>Design + Build</small></span>
    </div>
    <p class="front__web">www.ridgeway-db.com</p>
  </section>

  <section class="card card--back">
    <svg class="card__art" viewBox="0 0 700 400">
      <g role="img" aria-label="Large brand mark decoration area">
        <rect x="0" y="170" width="270" height="230" fill="var(--green)"/>
        <rect x="0" y="170" width="270" height="60" fill="var(--green-light)" opacity=".6"/>
        <rect x="110" y="200" width="60" height="70" fill="var(--ink)"/>
      </g>
      <path d="M0,348 C180,372 380,374 560,352 C400,388 200,400 0,400 Z" fill="var(--ink)"/>
    </svg>
    <div class="wordmark">
      <span class="wordmark__square"></span>
      <span class="wordmark__name">Ridgeway<small>Design + Build</small></span>
    </div>

    <div class="contact">
      <p class="contact__name">Jordan Hale</p>
      <p class="contact__title">Founder</p>
      <div class="contact__list">
        <p class="contact__line">
          <svg viewBox="0 0 16 16"><rect x="4" y="1" width="8" height="14" rx="1.5" fill="none" stroke="var(--green)" stroke-width="1.5"/></svg>
          <span>555-014-2290</span>
        </p>
        <p class="contact__line">
          <svg viewBox="0 0 16 16"><path d="M3,2 L6,2 L7,5 L5.5,6.5 C6.5,8.5 7.5,9.5 9.5,10.5 L11,9 L14,10 L14,13 C8,14 2,8 3,2 Z" fill="var(--green)"/></svg>
          <span>555-017-4400</span>
        </p>
        <p class="contact__line">
          <svg viewBox="0 0 16 16"><rect x="1" y="3" width="14" height="10" fill="var(--green)"/><path d="M1,3 L8,9 L15,3" fill="none" stroke="#fff" stroke-width="1.3"/></svg>
          <span>info@<span class="accent">ridgeway-db</span>.com</span>
        </p>
        <p class="contact__line">
          <svg viewBox="0 0 16 16" fill="none" stroke="var(--green)" stroke-width="1.3"><circle cx="8" cy="8" r="6.5"/><ellipse cx="8" cy="8" rx="3" ry="6.5"/><path d="M1.5,8 H14.5"/></svg>
          <span>www.<span class="accent">ridgeway-db</span>.com</span>
        </p>
      </div>
      <p class="contact__address">1420 Cedar Hollow Rd.<br>Pine Ridge, GA 30000</p>
    </div>
  </section>

</main>
</body>
</html>
```